Masonry and Landscaping Construction company business card

Looking for a business card design for a construction company named Ferrano Construction. It is an italian-american family business that specializes in custom stone work, patios, walkways, driveways, steps, outdoor kitchens, concrete, waterproofing, power wash, landscaping and more. Our colors are mostly red and white with some black. We're looking for a bold design. we also like to incorporate a picture of my family's hometown somewhere in it.
Target Market(s)
Luxury home owners
Industry/Entity Type
Construction
Contact Information for Business Card
Details includes should be bullet points mentioning the services provided. Custom Stone Work, Outdoor Kitchens, Fire Pits, Patios, Walkways, Steps, Concrete, Waterproofing, powerwash and landscaping
Requirements
Must have
- Would like a spot on the card for co-owners names, numbers and email to be listed also looking to add the QR code for an instagram page
Nice to have
- would like something bold, based around the colors red and white with black outlines or details

```html
<!DOCTYPE html>
<html lang="en">
<head>
<meta charset="utf-8">
<title>Ferrano Construction – Business Card</title>
<link rel="stylesheet" href="https://fonts.googleapis.com/css2?family=Roboto+Condensed:wght@500;700&family=Montserrat:wght@500;600&family=Lato:wght@400&display=swap">
<style>
  :root {
    --page-bg: #ffffff;
    --red-light: #d6292f;
    --red-dark: #ae1d23;
    --black-light: #262626;
    --black-dark: #121212;
    --white: #ffffff;
    --muted-white: #f1f1f1;
    --accent-red: #d8262c;
  }
  html, body {
    margin: 0;
    padding: 0;
    width: 1200px;
    height: 1000px;
    overflow: hidden;
    background: var(--page-bg);
  }
  .canvas {
    position: relative;
    width: 1200px;
    height: 1000px;
  }
  .card {
    position: absolute;
    left: 187px;
    width: 826px;
    height: 472px;
    border-radius: 18px;
    overflow: hidden;
  }
  .card--front {
    top: 22px;
    background: linear-gradient(90deg, var(--red-light) 0%, var(--red-dark) 100%);
  }
  .card--back {
    top: 507px;
    height: 471px;
    background: linear-gradient(115deg, var(--black-light) 0%, var(--black-dark) 55%, var(--black-light) 100%);
  }
  .brand {
    position: absolute;
    display: flex;
    align-items: center;
    gap: 16px;
    font-family: "Roboto Condensed", sans-serif;
    font-weight: 700;
    color: var(--white);
    text-transform: uppercase;
    line-height: 1;
  }
  .brand__square {
    background: var(--white);
    flex: none;
  }
  .brand__name {
    display: flex;
    flex-direction: column;
  }
  .brand--front {
    left: 50%;
    top: 130px;
    transform: translateX(-50%);
    font-size: 56px;
    letter-spacing: 1px;
  }
  .brand--front .brand__square {
    width: 70px;
    height: 70px;
  }
  .brand--front .brand__sub {
    font-size: 31px;
    letter-spacing: 4px;
    margin-top: 6px;
  }
  .services {
    position: absolute;
    left: 0;
    right: 0;
    top: 350px;
    margin: 0;
    padding: 0;
    list-style: none;
    text-align: center;
    font-family: "Roboto Condensed", sans-serif;
    font-weight: 500;
    font-size: 20px;
    letter-spacing: 0.8px;
    line-height: 29.5px;
    color: var(--white);
    text-transform: uppercase;
  }
  .services li {
    display: block;
  }
  .dot {
    display: inline-block;
    width: 7px;
    height: 7px;
    border-radius: 50%;
    background: var(--white);
    margin: 0 9px;
    vertical-align: 4px;
  }
  .machine-art {
    position: absolute;
    left: 0;
    top: 90px;
    width: 460px;
    height: 240px;
    background: radial-gradient(ellipse at 55% 45%, rgba(80,80,80,0.45) 0%, rgba(60,60,60,0.2) 55%, rgba(40,40,40,0) 80%);
  }
  .brand--back {
    left: 490px;
    top: 92px;
    font-size: 38px;
    gap: 12px;
  }
  .brand--back .brand__square {
    width: 46px;
    height: 46px;
  }
  .brand--back .brand__sub {
    font-size: 21px;
    letter-spacing: 3px;
    margin-top: 5px;
  }
  .person {
    position: absolute;
    left: 0;
    top: 256px;
  }
  .person__bar {
    position: absolute;
    left: 0;
    top: 0;
    width: 12px;
    height: 65px;
    background: var(--accent-red);
    border-radius: 0 4px 4px 0;
  }
  .person__name {
    position: absolute;
    left: 31px;
    top: 0;
    margin: 0;
    white-space: nowrap;
    font-family: "Montserrat", sans-serif;
    font-weight: 600;
    font-size: 31px;
    letter-spacing: 0.5px;
    color: var(--white);
  }
  .person__role {
    position: absolute;
    left: 30px;
    top: 42px;
    margin: 0;
    white-space: nowrap;
    font-family: "Montserrat", sans-serif;
    font-weight: 500;
    font-size: 21px;
    color: var(--muted-white);
  }
  .contact {
    position: absolute;
    left: 490px;
    top: 256px;
    margin: 0;
    padding: 0;
    list-style: none;
    font-family: "Lato", sans-serif;
    font-size: 22px;
    color: var(--white);
    letter-spacing: 0.3px;
  }
  .contact__item {
    display: flex;
    align-items: flex-start;
    gap: 11px;
    margin-bottom: 8px;
    line-height: 29px;
  }
  .contact__icon {
    flex: none;
    width: 22px;
    height: 22px;
    margin-top: 4px;
    border-radius: 3px;
    background: var(--accent-red);
    display: flex;
    align-items: center;
    justify-content: center;
  }
</style>
</head>
<body>
<main class="canvas">

  <section class="card card--front" aria-label="Card front">
    <div class="brand brand--front">
      <span class="brand__square"></span>
      <span class="brand__name">
        <span>Ferrano</span>
        <span class="brand__sub">Construction</span>
      </span>
    </div>
    <ul class="services">
      <li>Custom Stone Work<span class="dot"></span>Outdoor Kitchens<span class="dot"></span>Fire Pits<span class="dot"></span>Patios</li>
      <li>Walkways<span class="dot"></span>Steps<span class="dot"></span>Concrete<span class="dot"></span>Waterproofing</li>
      <li>Powerwash and Landscaping</li>
    </ul>
  </section>

  <section class="card card--back" aria-label="Card back">
    <div class="machine-art" role="img" aria-label="Faint silhouette of an excavator arm and bucket"></div>

    <div class="brand brand--back">
      <span class="brand__square"></span>
      <span class="brand__name">
        <span>Ferrano</span>
        <span class="brand__sub">Construction</span>
      </span>
    </div>

    <div class="person">
      <span class="person__bar"></span>
      <h2 class="person__name">MARCO FERRANO</h2>
      <p class="person__role">Marketing Executive</p>
    </div>

    <ul class="contact">
      <li class="contact__item">
        <span class="contact__icon">
          <svg width="14" height="14" viewBox="0 0 24 24" aria-hidden="true"><path fill="#fff" d="M6.6 10.8a15.1 15.1 0 0 0 6.6 6.6l2.2-2.2a1 1 0 0 1 1-.25 11.4 11.4 0 0 0 3.6.57 1 1 0 0 1 1 1V20a1 1 0 0 1-1 1A17 17 0 0 1 3 4a1 1 0 0 1 1-1h3.5a1 1 0 0 1 1 1c0 1.25.2 2.45.57 3.57a1 1 0 0 1-.25 1z"/></svg>
        </span>
        <span>055-318 742 906</span>
      </li>
      <li class="contact__item">
        <span class="contact__icon">
          <svg width="14" height="14" viewBox="0 0 24 24" aria-hidden="true"><path fill="#fff" d="M2 11 22 2l-9 20-2-9z"/></svg>
        </span>
        <span>hello@ferranobuild.com</span>
      </li>
      <li class="contact__item">
        <span class="contact__icon">
          <svg width="15" height="15" viewBox="0 0 24 24" aria-hidden="true"><g fill="none" stroke="#fff" stroke-width="2"><circle cx="12" cy="12" r="9"/><ellipse cx="12" cy="12" rx="4" ry="9"/><path d="M3 12h18"/></g></svg>
        </span>
        <span>www.ferranobuild.com</span>
      </li>
      <li class="contact__item">
        <span class="contact__icon">
          <svg width="14" height="14" viewBox="0 0 24 24" aria-hidden="true"><path fill="#fff" d="M12 2a7 7 0 0 0-7 7c0 5 7 13 7 13s7-8 7-13a7 7 0 0 0-7-7zm0 9.5A2.5 2.5 0 1 1 12 6.5a2.5 2.5 0 0 1 0 5z"/></svg>
        </span>
        <span>4471 Harbor Stone<br>Blvd, 212-C, FL 32461</span>
      </li>
    </ul>
  </section>

</main>
</body>
</html>
```